Infographics breakdown for small group

An infographic is needed to display the different personality types from a spreadsheet for 18 individuals. Name of the organization: Riverstone Harvest Fellowship Atlanta

Infographics of an Excel spreadsheet for 19 people at a church. The name of the church is Riverstone Harvest Fellowhsip Atlanta.

Target Market(s)

Church group

Industry/Entity Type

Spirtual

Requirements
Must have
• Age, Personality, and Spiritual Gifts breakdown
Nice to have
• Compelling photo,
Should not have
• I'm okay with the designer deciding

```html
<!DOCTYPE html>
<html lang="en">
<head>
<meta charset="utf-8">
<title>Personality Types – Riverstone Harvest Fellowship Atlanta</title>
<link href="https://fonts.googleapis.com/css2?family=Oswald:wght@500;700&family=Open+Sans:wght@400;600;700&display=swap" rel="stylesheet">
<style>
  :root{
    --bg:#3a1d5c;
    --bg-deep:#2a1245;
    --card:#321852;
    --band:#5b2d8c;
    --band-light:#7a45ad;
    --gold:#e5a823;
    --text:#ffffff;
    --muted:#c9b6e0;
  }
  *{box-sizing:border-box;margin:0;padding:0}
  html,body{width:667px;height:1200px;overflow:hidden;background:var(--bg-deep)}
  .poster{
    width:667px;height:1200px;position:relative;overflow:hidden;
    background:linear-gradient(180deg,var(--bg) 0%,var(--bg-deep) 100%);
    font-family:"Open Sans",sans-serif;color:var(--text);
  }
  .header{height:196px;position:relative}
  .header-sweep{position:absolute;left:0;top:128px;width:667px;height:60px}
  .ministry-mark{
    position:absolute;left:22px;top:18px;width:140px;height:150px;
    display:flex;flex-direction:column;align-items:center;justify-content:center;gap:10px;
    background:var(--bg-deep);
  }
  .ministry-mark .dot{width:44px;height:44px;border-radius:50%;background:var(--gold)}
  .ministry-mark .name{font-family:"Oswald",sans-serif;font-weight:700;font-size:17px;color:var(--gold);text-align:center}
  .church-mark{position:absolute;right:22px;top:24px;display:flex;align-items:center;gap:6px;background:#fff;padding:8px 10px}
  .church-mark .square{width:14px;height:14px;background:var(--band)}
  .church-mark .name{font-weight:700;font-size:13px;color:var(--band)}
  .title{
    position:absolute;left:200px;top:78px;
    font-family:"Oswald",sans-serif;font-weight:700;font-size:36px;letter-spacing:1px;
  }
  .grid{
    position:absolute;left:24px;top:204px;width:619px;height:976px;
    display:grid;grid-template-columns:repeat(5,1fr);grid-template-rows:repeat(4,1fr);gap:10px 8px;
  }
  .card{background:var(--card);display:flex;flex-direction:column;font-size:6.2px;line-height:1.45}
  .card-head{display:flex;align-items:center;justify-content:center;gap:4px;padding:7px 4px 5px}
  .card-head .icon{width:9px;height:9px;border-radius:50%;background:var(--gold)}
  .card-head .member{background:var(--gold);color:var(--bg-deep);font-weight:700;font-size:6.5px;padding:1px 5px}
  .contact{padding:3px 8px;color:var(--muted)}
  .contact li{list-style:none;display:flex;align-items:center;gap:3px}
  .contact li::before{content:"";width:4px;height:4px;border-radius:50%;background:var(--gold)}
  .band{background:var(--band);font-family:"Oswald",sans-serif;font-weight:500;font-size:7px;padding:2px 8px;margin-top:4px;letter-spacing:.4px}
  .band.type{background:var(--band-light)}
  .traits{padding:4px 8px 2px 16px;color:var(--muted)}
  .traits li{list-style:square}
  .foot{padding:5px 8px 7px;font-weight:700;font-size:5.8px;text-transform:uppercase;margin-top:auto}
</style>
</head>
<body>
<main class="poster">
  <header class="header">
    <svg class="header-sweep" viewBox="0 0 667 60" preserveAspectRatio="none" aria-hidden="true">
      <path d="M0 30 L667 8 L667 40 L0 58 Z" fill="#6b3a9c" opacity=".55"/>
      <path d="M0 42 L667 22 L667 30 L0 52 Z" fill="#8e5cc2" opacity=".5"/>
    </svg>
    <div class="ministry-mark"><span class="dot"></span><span class="name">Harvest Circle</span></div>
    <div class="church-mark"><span class="square"></span><span class="name">Riverstone Harvest</span></div>
    <h1 class="title">PERSONALITY TYPES</h1>
  </header>

  <section class="grid">
    <article class="card"><div class="card-head"><span class="icon"></span><span class="member">Member 01</span></div><ul class="contact"><li>Atlanta, Georgia USA</li><li>group@riverstonehf.org</li><li>404-555-0118</li></ul><div class="band">AGE 34</div><ul class="traits"><li>Dependable</li><li>Organized</li><li>Practical</li><li>Loyal</li><li>Calm</li></ul><div class="band type">TYPE ISTJ</div><p class="foot">Spiritual gifts: teaching, service, mercy<br>Small group leader since 2019</p></article>
    <article class="card"><div class="card-head"><span class="icon"></span><span class="member">Member 02</span></div><ul class="contact"><li>Atlanta, Georgia USA</li><li>group@riverstonehf.org</li><li>404-555-0118</li></ul><div class="band">AGE 27</div><ul class="traits"><li>Warm</li><li>Outgoing</li><li>Caring</li><li>Social</li><li>Helpful</li></ul><div class="band type">TYPE ESFJ</div><p class="foot">Spiritual gifts: hospitality, mercy, giving<br>Small group member since 2020</p></article>
    <article class="card"><div class="card-head"><span class="icon"></span><span class="member">Member 03</span></div><ul class="contact"><li>Atlanta, Georgia USA</li><li>group@riverstonehf.org</li><li>404-555-0118</li></ul><div class="band">AGE 45</div><ul class="traits"><li>Visionary</li><li>Driven</li><li>Decisive</li><li>Bold</li><li>Strategic</li></ul><div class="band type">TYPE ENTJ</div><p class="foot">Spiritual gifts: leadership, faith, wisdom<br>Small group member since 2016</p></article>
    <article class="card"><div class="card-head"><span class="icon"></span><span class="member">Member 04</span></div><ul class="contact"><li>Atlanta, Georgia USA</li><li>group@riverstonehf.org</li><li>404-555-0118</li></ul><div class="band">AGE 31</div><ul class="traits"><li>Gentle</li><li>Creative</li><li>Idealistic</li><li>Quiet</li><li>Kind</li></ul><div class="band type">TYPE INFP</div><p class="foot">Spiritual gifts: encouragement, mercy, music<br>Small group member since 2021</p></article>
    <article class="card"><div class="card-head"><span class="icon"></span><span class="member">Member 05</span></div><ul class="contact"><li>Atlanta, Georgia USA</li><li>group@riverstonehf.org</li><li>404-555-0118</li></ul><div class="band">AGE 52</div><ul class="traits"><li>Steady</li><li>Patient</li><li>Devoted</li><li>Humble</li><li>Careful</li></ul><div class="band type">TYPE ISFJ</div><p class="foot">Spiritual gifts: service, giving, intercession<br>Small group member since 2015</p></article>

    <article class="card"><div class="card-head"><span class="icon"></span><span class="member">Member 06</span></div><ul class="contact"><li>Atlanta, Georgia USA</li><li>group@riverstonehf.org</li><li>404-555-0118</li></ul><div class="band">AGE 23</div><ul class="traits"><li>Energetic</li><li>Playful</li><li>Curious</li><li>Spontaneous</li><li>Friendly</li></ul><div class="band type">TYPE ENFP</div><p class="foot">Spiritual gifts: evangelism, faith, worship<br>Small group member since 2022</p></article>
    <article class="card"><div class="card-head"><span class="icon"></span><span class="member">Member 07</span></div><ul class="contact"><li>Atlanta, Georgia USA</li><li>group@riverstonehf.org</li><li>404-555-0118</li></ul><div class="band">AGE 38</div><ul class="traits"><li>Logical</li><li>Analytical</li><li>Focused</li><li>Honest</li><li>Reserved</li></ul><div class="band type">TYPE INTJ</div><p class="foot">Spiritual gifts: knowledge, teaching, wisdom<br>Small group member since 2018</p></article>
    <article class="card"><div class="card-head"><span class="icon"></span><span class="member">Member 08</span></div><ul class="contact"><li>Atlanta, Georgia USA</li><li>group@riverstonehf.org</li><li>404-555-0118</li></ul><div class="band">AGE 41</div><ul class="traits"><li>Direct</li><li>Efficient</li><li>Responsible</li><li>Firm</li><li>Orderly</li></ul><div class="band type">TYPE ESTJ</div><p class="foot">Spiritual gifts: administration, leadership, giving<br>Small group member since 2017</p></article>
    <article class="card"><div class="card-head"><span class="icon"></span><span class="member">Member 09</span></div><ul class="contact"><li>Atlanta, Georgia USA</li><li>group@riverstonehf.org</li><li>404-555-0118</li></ul><div class="band">AGE 29</div><ul class="traits"><li>Insightful</li><li>Compassionate</li><li>Private</li><li>Deep</li><li>Principled</li></ul><div class="band type">TYPE INFJ</div><p class="foot">Spiritual gifts: discernment, prophecy, mercy<br>Small group member since 2020</p></article>
    <article class="card"><div class="card-head"><span class="icon"></span><span class="member">Member 10</span></div><ul class="contact"><li>Atlanta, Georgia USA</li><li>group@riverstonehf.org</li><li>404-555-0118</li></ul><div class="band">AGE 56</div><ul class="traits"><li>Adaptable</li><li>Hands-on</li><li>Calm</li><li>Observant</li><li>Skilled</li></ul><div class="band type">TYPE ISTP</div><p class="foot">Spiritual gifts: craftsmanship, service, helps<br>Small group member since 2014</p></article>

    <article class="card"><div class="card-head"><span class="icon"></span><span class="member">Member 11</span></div><ul class="contact"><li>Atlanta, Georgia USA</li><li>group@riverstonehf.org</li><li>404-555-0118</li></ul><div class="band">AGE 33</div><ul class="traits"><li>Inspiring</li><li>Empathetic</li><li>Persuasive</li><li>Warm</li><li>Loyal</li></ul><div class="band type">TYPE ENFJ</div><p class="foot">Spiritual gifts: shepherding, exhortation, teaching<br>Small group member since 2019</p></article>
    <article class="card"><div class="card-head"><span class="icon"></span><span class="member">Member 12</span></div><ul class="contact"><li>Atlanta, Georgia USA</li><li>group@riverstonehf.org</li><li>404-555-0118</li></ul><div class="band">AGE 48</div><ul class="traits"><li>Lively</li><li>Fun</li><li>Generous</li><li>Bright</li><li>Open</li></ul><div class="band type">TYPE ESFP</div><p class="foot">Spiritual gifts: hospitality, worship, giving<br>Small group member since 2016</p></article>
    <article class="card"><div class="card-head"><span class="icon"></span><span class="member">Member 13</span></div><ul class="contact"><li>Atlanta, Georgia USA</li><li>group@riverstonehf.org</li><li>404-555-0118</li></ul><div class="band">AGE 26</div><ul class="traits"><li>Inventive</li><li>Witty</li><li>Curious</li><li>Quick</li><li>Debater</li></ul><div class="band type">TYPE ENTP</div><p class="foot">Spiritual gifts: apostleship, faith, knowledge<br>Small group member since 2022</p></article>
    <article class="card"><div class="card-head"><span class="icon"></span><span class="member">Member 14</span></div><ul class="contact"><li>Atlanta, Georgia USA</li><li>group@riverstonehf.org</li><li>404-555-0118</li></ul><div class="band">AGE 61</div><ul class="traits"><li>Faithful</li><li>Thorough</li><li>Reliable</li><li>Wise</li><li>Steady</li></ul><div class="band type">TYPE ISTJ</div><p class="foot">Spiritual gifts: wisdom, intercession, teaching<br>Small group member since 2012</p></article>
    <article class="card"><div class="card-head"><span class="icon"></span><span class="member">Member 15</span></div><ul class="contact"><li>Atlanta, Georgia USA</li><li>group@riverstonehf.org</li><li>404-555-0118</li></ul><div class="band">AGE 36</div><ul class="traits"><li>Artistic</li><li>Sensitive</li><li>Gentle</li><li>Humble</li><li>Present</li></ul><div class="band type">TYPE ISFP</div><p class="foot">Spiritual gifts: music, mercy, encouragement<br>Small group member since 2019</p></article>

    <article class="card"><div class="card-head"><span class="icon"></span><span class="member">Member 16</span></div><ul class="contact"><li>Atlanta, Georgia USA</li><li>group@riverstonehf.org</li><li>404-555-0118</li></ul><div class="band">AGE 44</div><ul class="traits"><li>Practical</li><li>Active</li><li>Bold</li><li>Resourceful</li><li>Direct</li></ul><div class="band type">TYPE ESTP</div><p class="foot">Spiritual gifts: evangelism, helps, leadership<br>Small group member since 2018</p></article>
    <article class="card"><div class="card-head"><span class="icon"></span><span class="member">Member 17</span></div><ul class="contact"><li>Atlanta, Georgia USA</li><li>group@riverstonehf.org</li><li>404-555-0118</li></ul><div class="band">AGE 30</div><ul class="traits"><li>Thoughtful</li><li>Precise</li><li>Independent</li><li>Curious</li><li>Quiet</li></ul><div class="band type">TYPE INTP</div><p class="foot">Spiritual gifts: knowledge, discernment, teaching<br>Small group member since 2021</p></article>
    <article class="card"><div class="card-head"><span class="icon"></span><span class="member">Member 18</span></div><ul class="contact"><li>Atlanta, Georgia USA</li><li>group@riverstonehf.org</li><li>404-555-0118</li></ul><div class="band">AGE 39</div><ul class="traits"><li>Nurturing</li><li>Cheerful</li><li>Attentive</li><li>Loyal</li><li>Caring</li></ul><div class="band type">TYPE ESFJ</div><p class="foot">Spiritual gifts: hospitality, service, mercy<br>Small group member since 2017</p></article>
    <article class="card"><div class="card-head"><span class="icon"></span><span class="member">Member 19</span></div><ul class="contact"><li>Atlanta, Georgia USA</li><li>group@riverstonehf.org</li><li>404-555-0118</li></ul><div class="band">AGE 58</div><ul class="traits"><li>Patient</li><li>Kind</li><li>Supportive</li><li>Modest</li><li>Faithful</li></ul><div class="band type">TYPE ISFJ</div><p class="foot">Spiritual gifts: intercession, giving, helps<br>Small group member since 2013</p></article>
    <article class="card"><div class="card-head"><span class="icon"></span><span class="member">Member 20</span></div><ul class="contact"><li>Atlanta, Georgia USA</li><li>group@riverstonehf.org</li><li>404-555-0118</li></ul><div class="band">AGE 25</div><ul class="traits"><li>Hopeful</li><li>Eager</li><li>Friendly</li><li>Creative</li><li>Open</li></ul><div class="band type">TYPE ENFP</div><p class="foot">Spiritual gifts: worship, evangelism, faith<br>Small group member since 2023</p></article>
  </section>
</main>
</body>
</html>
```